Business Card Design Project 4 Construction Business

I am after a creative, but sleek and simple/ clean business card design. This design will form the basis of future items and might include a logo or simply a creative way to lay out the text of my company name 'keldmoor builds'
I like the simplicity of black and white however I would also be happy to see a splash of colour introduced somehow to give the text some interest and make it stand out.
I would like a double sided card.
I am young (ish!) and professional, offering construction and project management services, what I don't want is the traditional builders type card featuring a cheesy hammer/ saw image etc.
As the company name, keldmoor builds, suggests, we focus on working closely and collaboratively together, in synergy with all stakeholders involved in the projects that we undertake
Industry/Entity Type
Construction

```html
<!DOCTYPE html>
<html lang="en">
<head>
<meta charset="utf-8">
<title>Keldmoor Builds – Business Card</title>
<link rel="stylesheet" href="https://fonts.googleapis.com/css2?family=Arimo:wght@400;700&display=swap">
<style>
  :root {
    --backdrop: #dcdcdc;
    --card: #ffffff;
    --ink: #111111;
    --ink-soft: #444444;
    --ink-muted: #5a5a5a;
    --rule: #b5b5b5;
    --hazard-yellow: #f6c21c;
  }
  * { box-sizing: border-box; margin: 0; padding: 0; }
  html, body {
    width: 1200px;
    height: 1000px;
    overflow: hidden;
  }
  body {
    background: radial-gradient(ellipse at 50% 45%, #f2f2f2 0%, var(--backdrop) 100%);
    font-family: "Arimo", Arial, sans-serif;
    color: var(--ink);
    position: relative;
  }
  .card {
    position: absolute;
    width: 720px;
    height: 420px;
    background: var(--card);
    box-shadow: 0 4px 10px rgba(0,0,0,0.18);
  }
  /* Front side */
  .card--front { left: 60px; top: 90px; }
  .wordmark {
    font-family: "Arimo", Arial, sans-serif;
    font-weight: 700;
    color: var(--ink);
    text-transform: uppercase;
    line-height: 1;
  }
  .card--front .wordmark {
    position: absolute;
    left: 0;
    right: 0;
    top: 140px;
    text-align: center;
  }
  .wordmark__line { display: block; }
  .wordmark__line--main { font-size: 56px; letter-spacing: 2px; }
  .wordmark__line--sub { font-size: 26px; letter-spacing: 24px; margin-top: 10px; padding-left: 24px; }
  .hazard-band {
    position: absolute;
    left: 0;
    right: 0;
    top: 318px;
    height: 30px;
    display: block;
  }
  .card--front .site-url {
    position: absolute;
    right: 120px;
    top: 362px;
    font-size: 20px;
    letter-spacing: 1.5px;
    color: var(--ink);
  }
  /* Back side */
  .card--back { left: 420px; top: 530px; }
  .card--back .wordmark {
    position: absolute;
    left: 60px;
    top: 160px;
    width: 280px;
    text-align: center;
  }
  .card--back .wordmark__line--main { font-size: 34px; letter-spacing: 1px; }
  .card--back .wordmark__line--sub { font-size: 16px; letter-spacing: 14px; padding-left: 14px; margin-top: 6px; }
  .divider {
    position: absolute;
    left: 370px;
    top: 80px;
    width: 2px;
    height: 240px;
    background: var(--rule);
  }
  .contact {
    position: absolute;
    left: 395px;
    top: 92px;
    color: var(--ink-soft);
  }
  .contact__name { font-size: 30px; font-weight: 400; letter-spacing: 1.5px; color: var(--ink-muted); }
  .contact__role { font-size: 17px; letter-spacing: 1px; margin-top: 2px; }
  .contact__lines { list-style: none; margin-top: 42px; font-size: 14px; letter-spacing: 1px; line-height: 1.3; }
  .contact__address { margin-top: 12px; font-size: 13px; letter-spacing: 0.5px; }
</style>
</head>
<body>
  <section class="card card--front" aria-label="Card front">
    <h1 class="wordmark">
      <span class="wordmark__line wordmark__line--main">Keldmoor</span>
      <span class="wordmark__line wordmark__line--sub">Builds</span>
    </h1>
    <svg class="hazard-band" role="img" aria-label="Black and yellow diagonal hazard stripe band" viewBox="0 0 720 30" preserveAspectRatio="none">
      <rect x="0" y="0" width="720" height="30" fill="var(--hazard-yellow)"/>
    </svg>
    <p class="site-url">www.keldmoorbuilds.com.au</p>
  </section>

  <section class="card card--back" aria-label="Card back">
    <p class="wordmark">
      <span class="wordmark__line wordmark__line--main">Keldmoor</span>
      <span class="wordmark__line wordmark__line--sub">Builds</span>
    </p>
    <div class="divider"></div>
    <div class="contact">
      <h2 class="contact__name">Tomas Brenner</h2>
      <p class="contact__role">Director</p>
      <ul class="contact__lines">
        <li>0400 555 019</li>
        <li>tomas@keldmoorbuilds.com.au</li>
        <li>www.keldmoorbuilds.com.au</li>
      </ul>
      <p class="contact__address">Address: 12 Harlow St Northbay NSW 2199</p>
    </div>
  </section>
</body>
</html>
```